KWB needs a professional PP

We are looking for a more professional powerpoint presentation that will be presented to prospective clients. This powerpoint needs to summarize all the services and value that The Harbinger Collective has to offer, pretty much giving an overview of the company.

The clients we deal with are Funeral Homes and Funeral Directors, we are an organization dedicated to assisting funeral homes in implementing highly profitable insurance programs while providing the training, support and service along the way. More information is provided in the brochure attached.

We are going for a professional simple theme, we want to get the message across without overwhelming the client.

I have attached our current powerpoint presentation as reference and more information about the our company and what we offer. This one is obviously what we are looking to replace, but the information will be generally the same. It needs to be more visually appealing and convey professionalism.

```html
<!DOCTYPE html>
<html lang="en">
<head>
<meta charset="utf-8">
<title>The Harbinger Collective – Presentation</title>
<link rel="stylesheet" href="https://fonts.googleapis.com/css2?family=Libre+Baskerville&family=Tinos:wght@400;700&family=Source+Sans+3:ital,wght@1,300&display=swap">
<style>
  :root{
    --stage:#000;
    --navy:#0d56a6;
    --navy-soft:#3a7cc4;
    --title:#23508f;
    --ink:#1c1c1c;
    --slate:#5a6a80;
    --paper:#f2f2f2;
    --paper-dark:#d9d9d9;
    --panel:#f3f3f3;
    --icon:#7ea5d4;
    --callout:#e3ebf5;
  }
  *{box-sizing:border-box;margin:0;padding:0}
  html,body{width:1200px;height:1000px;overflow:hidden;background:var(--stage)}
  .canvas{position:relative;width:1200px;height:1000px}
  .slide{position:absolute;width:565px;height:421px;overflow:hidden;
    background:linear-gradient(180deg,#f6f6f6 0%,#e9e9e9 60%,#dcdcdc 100%);
    font-family:"Tinos",serif;color:var(--ink)}
  .s1{left:23px;top:57px}.s2{left:613px;top:57px}.s3{left:25px;top:535px}.s4{left:613px;top:535px}

  /* cover */
  .cover-band{position:absolute;left:0;right:0;top:120px;height:181px;background:var(--paper);box-shadow:0 2px 6px rgba(0,0,0,.12)}
  .cover-bar{position:absolute;left:94px;width:382px;height:8px;background:var(--navy)}
  .cover-bar.top{top:111px}.cover-bar.bottom{top:301px}
  .cover-name{position:absolute;left:0;right:0;top:165px;text-align:center;font-family:"Libre Baskerville",serif;font-size:27px;color:var(--slate);letter-spacing:.5px}
  .cover-sub{position:absolute;left:0;right:0;top:245px;text-align:center;font-size:15px;color:var(--navy-soft)}

  /* shared content slide */
  .topbar{position:absolute;left:0;right:0;top:0;height:10px;background:var(--navy)}
  .topbar::after{content:"";position:absolute;left:46px;top:0;width:114px;height:10px;background:var(--navy-soft)}
  .slide-title{position:absolute;left:18px;top:28px;font-family:"Libre Baskerville",serif;font-variant:small-caps;font-size:26px;color:var(--title);letter-spacing:.3px}
  .footer{position:absolute;left:0;right:0;bottom:0;height:38px;background:#fafafa}
  .footer-name{position:absolute;left:22px;top:12px;font-family:"Libre Baskerville",serif;font-size:11px;color:var(--slate);border-bottom:1px solid var(--slate)}
  .page-no{position:absolute;right:20px;top:13px;font-size:10px;color:#888}

  /* about */
  .about-list{position:absolute;left:36px;top:88px;width:510px;list-style:none;font-size:17.5px;line-height:27px}
  .about-list li{position:relative;padding-left:17px;margin-bottom:6px}
  .about-list li::before,.rep-list li::before{content:"";position:absolute;left:0;top:10px;border-left:6px solid var(--navy);border-top:4px solid transparent;border-bottom:4px solid transparent}
  .callout{position:absolute;left:222px;top:290px;width:343px;height:80px}
  .callout-bar{position:absolute;right:0;width:155px;height:8px;background:var(--navy)}
  .callout-bar.top{top:281px}.callout-bar.bottom{top:370px}
  .tagline{position:absolute;right:30px;top:296px;font-family:"Source Sans 3",sans-serif;font-style:italic;font-weight:300;font-size:17px;line-height:23px;color:var(--title)}
  .tagline span{display:block}
  .tagline .l1{margin-right:52px}.tagline .l2{margin-right:28px}

  /* partners */
  .rep-panel{position:absolute;left:180px;width:340px;height:112px;background:var(--panel);box-shadow:0 3px 6px rgba(0,0,0,.18)}
  .rep-badge{position:absolute;left:40px;width:132px;height:132px;border:4px solid var(--navy);border-radius:50% 0 50% 50%;background:#fff;display:flex;align-items:center;justify-content:center;box-shadow:0 3px 6px rgba(0,0,0,.18)}
  .rep-name{font-size:19px;color:var(--navy);text-align:center;line-height:1.1}
  .rep-list{position:absolute;left:218px;width:290px;list-style:none;font-size:13px;line-height:17.5px}
  .rep-list li{position:relative;padding-left:18px}
  .rep-list li::before{top:5px;border-left-width:5px;border-top-width:3px;border-bottom-width:3px;border-left-color:var(--navy-soft)}

  /* final expense */
  .col-head{position:absolute;top:72px;width:232px;height:26px;background:var(--navy-soft);color:#fff;text-align:center;font-family:"Libre Baskerville",serif;font-variant:small-caps;font-size:16px;line-height:26px}
  .col-head::after{content:"";position:absolute;left:50%;bottom:-7px;margin-left:-7px;border-top:7px solid var(--navy-soft);border-left:7px solid transparent;border-right:7px solid transparent}
  .card{position:absolute;width:232px;background:var(--panel);box-shadow:0 3px 6px rgba(0,0,0,.22);padding:9px 8px 0 8px;font-size:10px;line-height:12.5px}
  .row{display:flex;align-items:center;gap:7px;margin-bottom:8px}
  .row.top{align-items:flex-start}
  .icon{flex:none;width:21px;height:21px;border-radius:50%;background:var(--icon);color:#fff;display:flex;align-items:center;justify-content:center;font-size:12px;font-weight:700}
  .note{font-size:8px}
  .footnote{position:absolute;left:48px;top:368px;font-size:8.3px}
</style>
</head>
<body>
<div class="canvas">

  <section class="slide s1">
    <div class="cover-band"></div>
    <div class="cover-bar top"></div>
    <div class="cover-bar bottom"></div>
    <div class="cover-name">The Harbinger Collective</div>
    <div class="cover-sub">Insurance Management Consultants</div>
  </section>

  <section class="slide s2">
    <div class="topbar"></div>
    <h1 class="slide-title">About The Harbinger Collective</h1>
    <ul class="about-list">
      <li>Insurance Management Consulting Firm</li>
      <li>Provide alternative options for costs of burial</li>
      <li>Provide consulting on maximizing revenue streams from insurance sales and bonuses</li>
      <li>Specialize in Final Expense and Advanced Wealth Transfer</li>
    </ul>
    <svg class="callout" viewBox="0 0 343 80" aria-hidden="true"><polygon points="40,0 343,0 343,80 40,80 0,40" fill="var(--callout)"/></svg>
    <div class="callout-bar top"></div>
    <div class="callout-bar bottom"></div>
    <p class="tagline"><span class="l1">Become more profitable.</span><span class="l2">More successful.</span><span>More secure.</span></p>
    <footer class="footer"><span class="footer-name">The Harbinger Collective</span><span class="page-no">2</span></footer>
  </section>

  <section class="slide s3">
    <div class="topbar"></div>
    <h1 class="slide-title">Who We Represent</h1>
    <div class="rep-panel" style="top:93px"></div>
    <div class="rep-badge" style="top:84px"><span class="rep-name">Larchmont<br>Life</span></div>
    <ul class="rep-list" style="top:111px">
      <li>Competitively low rates</li>
      <li>Broad coverage</li>
      <li>Instant approval over the phone</li>
      <li>Monthly or single premium available</li>
    </ul>
    <div class="rep-panel" style="top:240px"></div>
    <div class="rep-badge" style="top:230px"><span class="rep-name">Evergrove</span></div>
    <ul class="rep-list" style="top:259px">
      <li>Relaxed underwriting</li>
      <li>Application and approval done over the phone</li>
      <li>Instant approval</li>
    </ul>
    <footer class="footer"><span class="footer-name">The Harbinger Collective</span><span class="page-no">3</span></footer>
  </section>

  <section class="slide s4">
    <div class="topbar"></div>
    <h1 class="slide-title">Final Expense</h1>
    <div class="col-head" style="left:42px">Final Expense</div>
    <div class="col-head" style="left:303px">Single Premium</div>

    <div class="card" style="left:42px;top:117px;height:116px">
      <div class="row top"><span class="icon"><svg width="11" height="11" viewBox="0 0 11 11"><path d="M2 9 L9 2" stroke="#fff" stroke-width="2.2" stroke-linecap="round"/></svg></span><span>Write a final expense product for the amount of the funeral and adjust for future inflation</span></div>
      <div class="row"><span class="icon">$</span><span>$7,000 Funeral → $10,000 Policy</span></div>
      <div class="row"><span class="icon">%</span><span>60%* commission</span></div>
    </div>
    <div class="card" style="left:42px;top:237px;height:118px">
      <div class="row top"><span class="icon"><svg width="11" height="11" viewBox="0 0 11 11"><path d="M2 9 L9 2" stroke="#fff" stroke-width="2.2" stroke-linecap="round"/></svg></span><span>Write a final expense product for a set amount and give the family an allowance to use</span></div>
      <div class="row"><span class="icon">$</span><span>$10,000 Policy → $10,000 Allowance</span></div>
      <div class="row"><span class="icon">%</span><span>60%* commission</span></div>
    </div>
    <div class="card" style="left:303px;top:117px;height:116px">
      <div class="row"><span class="icon"><svg width="12" height="12" viewBox="0 0 12 12"><circle cx="6" cy="6" r="4.5" fill="none" stroke="#fff" stroke-width="1.3"/><path d="M6 3.5 V6 H8" fill="none" stroke="#fff" stroke-width="1.3"/></svg></span><span>Family pays for funeral upfront</span></div>
      <div class="row"><span class="icon">$</span><span>$10,000 premium → $17,509 in coverage<br><span class="note">(Based on 65 year old, non-smoking, female)</span></span></div>
      <div class="row"><span class="icon">%</span><span>9% commission</span></div>
    </div>
    <p class="footnote">*Commission for final expense products will increase from the base commission of 60% in relation to total monthly production</p>
    <footer class="footer"><span class="footer-name">The Harbinger Collective</span><span class="page-no">4</span></footer>
  </section>

</div>
</body>
</html>
```